Business Card Design Project

Company name will be Tolvan Crest (named after my black lab and his fraying muzzle) Business is in the body armor, Security product industry servicing the state, local, and federal law enforcement markets. I want a more formal and serious logo for both business cards and letterhead

```html
<!DOCTYPE html>
<html lang="en">
<head>
<meta charset="utf-8">
<title>Tolvan Crest – Business Card</title>
<link rel="stylesheet" href="https://fonts.googleapis.com/css2?family=Exo+2:wght@300;600&display=swap">
<style>
  :root {
    --page-bg: #dcdad6;
    --card-top: #eef6fd;
    --card-bottom: #f5f6f8;
    --brand-grey: #58585b;
    --text-dark: #3a3a3c;
    --accent-blue: #2f6fc0;
    --accent-light: #8fb3de;
  }
  * { margin: 0; padding: 0; box-sizing: border-box; }
  html, body {
    width: 1200px; height: 803px; overflow: hidden;
    background: var(--page-bg);
    font-family: "Exo 2", sans-serif;
  }
  .card {
    position: absolute; left: 80px; top: 101px;
    width: 1040px; height: 600px;
    background: linear-gradient(160deg, var(--card-top), var(--card-bottom));
    box-shadow: 0 8px 24px rgba(0,0,0,0.18);
  }
  .brand-mark { position: absolute; left: 209px; top: 115px; width: 98px; height: 98px; }
  .brand-name {
    position: absolute; left: 343px; top: 115px;
    font-size: 88px; font-weight: 600; line-height: 1;
    color: var(--brand-grey); letter-spacing: -1px; white-space: nowrap;
  }
  .person {
    position: absolute; right: 573px; text-align: right;
    color: var(--text-dark); font-weight: 300; white-space: nowrap;
  }
  .person-name {
    top: 378px; font-size: 38px; line-height: 1;
    padding-bottom: 6px;
    border-bottom: 2px solid var(--accent-blue);
  }
  .person-title { top: 434px; font-size: 32px; line-height: 1; }
  .divider {
    position: absolute; left: 502px; top: 338px; width: 3px; height: 173px;
    background: linear-gradient(to bottom, var(--accent-light), var(--accent-blue), var(--accent-light));
  }
  .contact-list { position: absolute; left: 536px; top: 0; list-style: none; }
  .contact-item {
    position: absolute; left: 0; display: flex; align-items: center;
    font-size: 30px; font-weight: 300; line-height: 1;
    color: var(--text-dark); white-space: nowrap;
  }
  .contact-icon { width: 28px; height: 28px; margin-right: 12px; flex: none; }
  .contact-item.no-icon { padding-left: 40px; }
</style>
</head>
<body>
  <div class="card">
    <svg class="brand-mark" viewBox="0 0 98 98" aria-hidden="true">
      <circle cx="49" cy="49" r="49" fill="var(--accent-blue)"/>
    </svg>
    <div class="brand-name">Tolvan Crest</div>

    <div class="person person-name">Reid Calloway</div>
    <div class="person person-title">Manufacturers Rep Principal</div>

    <div class="divider"></div>

    <ul class="contact-list">
      <li class="contact-item" style="top:344px">
        <svg class="contact-icon" viewBox="0 0 28 28" aria-hidden="true">
          <circle cx="14" cy="14" r="12" fill="none" stroke="var(--accent-blue)" stroke-width="3"/>
          <circle cx="14" cy="14" r="5" fill="var(--accent-blue)"/>
        </svg>2710 Harbor Lane North
      </li>
      <li class="contact-item no-icon" style="top:384px">Marlow Beach, FL 32099</li>
      <li class="contact-item" style="top:426px">
        <svg class="contact-icon" viewBox="0 0 28 28" aria-hidden="true">
          <rect x="8" y="2" width="12" height="24" rx="2" fill="none" stroke="var(--accent-blue)" stroke-width="2.5"/>
          <rect x="11" y="6" width="6" height="7" fill="var(--accent-blue)"/>
          <circle cx="14" cy="20" r="2" fill="var(--accent-blue)"/>
        </svg>904-555-0173
      </li>
      <li class="contact-item" style="top:468px">
        <svg class="contact-icon" viewBox="0 0 28 28" aria-hidden="true">
          <rect x="2" y="3" width="24" height="17" rx="1.5" fill="var(--accent-blue)"/>
          <rect x="4.5" y="5.5" width="19" height="12" fill="var(--accent-light)"/>
          <rect x="12" y="20" width="4" height="4" fill="var(--accent-blue)"/>
          <rect x="8" y="24" width="12" height="2" fill="var(--accent-blue)"/>
        </svg>rcalloway.tc@mailbox.com
      </li>
    </ul>
  </div>
</body>
</html>
```